Business Card Tevan Law llc examples and ideas are attached.

in addition to the logo we need a desription what we do: "Reprsenting students with disabilites obtain services to progress in the public school system."

If you can squeeze it on the fron at the bottom great if not put it on the back

```html
<!DOCTYPE html>
<html lang="en">
<head>
<meta charset="utf-8">
<title>Tevan Law llc – Business Card</title>
<link rel="stylesheet" href="https://fonts.googleapis.com/css2?family=Roboto:ital,wght@0,400;0,500;1,400&display=swap">
<style>
  :root {
    --page-bg: #d9dadb;
    --card-bg: #000000;
    --brand-blue: #1fa7e8;
    --brand-yellow: #f4e82a;
    --brand-orange: #f7941d;
  }
  * { margin: 0; padding: 0; box-sizing: border-box; }
  html, body {
    width: 1200px;
    height: 900px;
    overflow: hidden;
    background: var(--page-bg);
    font-family: "Roboto", Arial, sans-serif;
  }
  .card {
    position: absolute;
    left: 75px;
    top: 150px;
    width: 1050px;
    height: 598px;
    background: var(--card-bg);
  }
  .brand-mark {
    position: absolute;
    left: 108px;
    top: 240px;
    display: flex;
    align-items: center;
    gap: 14px;
  }
  .brand-mark__square {
    width: 44px;
    height: 44px;
    background: var(--brand-orange);
  }
  .brand-mark__name {
    color: var(--brand-blue);
    font-size: 38px;
    font-weight: 500;
    white-space: nowrap;
  }
  .divider {
    position: absolute;
    left: 499px;
    top: 128px;
    width: 3px;
    height: 310px;
    background: var(--brand-yellow);
  }
  .firm-name {
    position: absolute;
    right: 62px;
    top: 80px;
    color: var(--brand-blue);
    font-size: 52px;
    font-weight: 400;
    text-transform: uppercase;
    white-space: nowrap;
  }
  .attorney-name {
    position: absolute;
    right: 62px;
    top: 178px;
    color: var(--brand-yellow);
    font-size: 30px;
    white-space: nowrap;
  }
  .attorney-title {
    position: absolute;
    right: 62px;
    top: 224px;
    color: var(--brand-blue);
    font-size: 30px;
    font-style: italic;
    white-space: nowrap;
  }
  .contact {
    position: absolute;
    left: 622px;
    display: flex;
    align-items: flex-start;
    gap: 30px;
    color: var(--brand-yellow);
    font-size: 23px;
    line-height: 31px;
  }
  .contact__icon { width: 26px; height: 28px; flex: none; margin-top: 1px; }
  .contact--address { top: 290px; }
  .contact--phone { top: 404px; }
  .contact--email { top: 462px; }
  .contact sup { font-size: 13px; }
  .tagline {
    position: absolute;
    left: 40px;
    right: 40px;
    bottom: 28px;
    color: var(--brand-blue);
    font-size: 19px;
    line-height: 24px;
    text-align: center;
    white-space: nowrap;
  }
</style>
</head>
<body>
  <div class="card">
    <div class="brand-mark">
      <span class="brand-mark__square"></span>
      <span class="brand-mark__name">Tevan Law llc</span>
    </div>

    <div class="divider"></div>

    <h1 class="firm-name">Tevan Law llc</h1>
    <p class="attorney-name">Daniel K Tevan&nbsp; MBA</p>
    <p class="attorney-title">Attorney at Law</p>

    <div class="contact contact--address">
      <svg class="contact__icon" viewBox="0 0 24 28" aria-hidden="true">
        <path d="M12 1C7 1 3.5 4.8 3.5 9.5 3.5 16 12 26 12 26s8.5-10 8.5-16.5C20.5 4.8 17 1 12 1z" fill="var(--brand-blue)"/>
        <circle cx="12" cy="9.5" r="3.2" fill="var(--card-bg)"/>
      </svg>
      <p>1480 SW 14<sup>th</sup> Ave<br>Coral Springs FL33065<br>By appointment only</p>
    </div>

    <div class="contact contact--phone">
      <svg class="contact__icon" viewBox="0 0 24 28" aria-hidden="true">
        <rect x="6" y="1" width="12" height="26" rx="3" fill="var(--brand-blue)"/>
        <rect x="8.5" y="5" width="7" height="15" fill="var(--card-bg)"/>
        <circle cx="12" cy="23.5" r="1.5" fill="var(--card-bg)"/>
      </svg>
      <p>555 014 2297</p>
    </div>

    <div class="contact contact--email">
      <svg class="contact__icon" viewBox="0 0 24 28" aria-hidden="true">
        <rect x="2" y="8" width="20" height="14" fill="none" stroke="var(--brand-blue)" stroke-width="2"/>
        <path d="M2 8l10 8 10-8" fill="none" stroke="var(--brand-blue)" stroke-width="2"/>
      </svg>
      <p>dan.tevanlaw@mail.com</p>
    </div>

    <p class="tagline">Representing students with disabilities obtain services to progress in the public school system.</p>
  </div>
</body>
</html>
```